Need a business card design for a new business

The business is going to be called "The Maple Lectern" - it is an online training company that provides Instructor Lead training to students at any destination in the world
The reference to cloud is the internet and classroom reference will be a computer at the students and instructors end

We will need a Web site and stationary and advertising material developed over time but for now require the business cards only

So if we are happy with the business card then we will use the same designers for the other requirments of the business as it evolves

Industry/Entity Type

Advertising

```html
<!DOCTYPE html>
<html lang="en">
<head>
<meta charset="utf-8">
<title>The Maple Lectern — Business Card</title>
<link rel="stylesheet" href="https://fonts.googleapis.com/css2?family=Tinos:ital,wght@0,400;0,700;1,400;1,700&family=Arimo:wght@400;700&display=swap">
<style>
  :root {
    --page-bg: #e9e7e1;
    --card-olive: #5a5a30;
    --card-olive-dark: #4c4c27;
    --accent-lime: #c4cc45;
    --accent-lime-soft: #8f9a35;
    --ink-cream: #f4f1e4;
    --ink-white: #ffffff;
    --icon-fill: #2f3a5a;
  }
  * { box-sizing: border-box; margin: 0; padding: 0; }
  html, body {
    width: 1200px;
    height: 996px;
    overflow: hidden;
    background: var(--page-bg);
  }
  .canvas {
    position: relative;
    width: 1200px;
    height: 996px;
  }
  .business-card {
    position: absolute;
    left: 75px;
    top: 198px;
    width: 1050px;
    height: 600px;
    background: var(--card-olive);
    box-shadow: 0 10px 30px rgba(0,0,0,0.25);
    overflow: hidden;
    font-family: "Tinos", "Times New Roman", serif;
    color: var(--ink-white);
  }
  .brand {
    position: absolute;
    left: 40px;
    top: 70px;
    display: flex;
    align-items: center;
    gap: 18px;
  }
  .brand-mark {
    width: 56px;
    height: 56px;
    border-radius: 50%;
    background: var(--ink-cream);
    flex: none;
  }
  .brand-name {
    font-family: "Tinos", "Times New Roman", serif;
    font-weight: 700;
    font-size: 58px;
    line-height: 1;
    color: var(--ink-cream);
    letter-spacing: 1px;
  }
  .web-address {
    position: absolute;
    right: 110px;
    top: 62px;
    font-size: 30px;
    letter-spacing: 2px;
    color: var(--accent-lime);
  }
  .wave-art {
    position: absolute;
    left: 470px;
    top: 125px;
    width: 530px;
    height: 420px;
    border-radius: 50% 40% 50% 45%;
    background: radial-gradient(ellipse at 50% 50%, var(--accent-lime-soft) 0%, rgba(143,154,53,0.45) 45%, rgba(90,90,48,0) 72%);
  }
  .person {
    position: absolute;
    left: 130px;
    top: 318px;
    text-align: right;
  }
  .person-name {
    font-size: 44px;
    line-height: 1.05;
    font-weight: 400;
  }
  .person-role {
    font-size: 26px;
    color: var(--ink-cream);
  }
  .contact-list {
    position: absolute;
    left: 750px;
    top: 300px;
    list-style: none;
    font-family: "Arimo", Arial, sans-serif;
    font-size: 19px;
  }
  .contact-item {
    display: flex;
    align-items: center;
    gap: 14px;
    height: 44px;
  }
  .contact-item.is-phone-alt { font-size: 24px; height: 54px; }
  .contact-icon {
    width: 30px;
    height: 30px;
    flex: none;
  }
  .address {
    position: absolute;
    left: 40px;
    bottom: 40px;
    font-family: "Arimo", Arial, sans-serif;
    font-size: 26px;
    line-height: 1.3;
  }
</style>
</head>
<body>
<main class="canvas">
  <article class="business-card">
    <div class="brand">
      <span class="brand-mark"></span>
      <h1 class="brand-name">The Maple Lectern</h1>
    </div>

    <p class="web-address">www.maplelectern.com</p>

    <div class="wave-art" role="img" aria-label="Decorative flowing line pattern in lime green"></div>

    <div class="person">
      <p class="person-name">Mr. Daniel Reyes</p>
      <p class="person-role">Executive</p>
    </div>

    <ul class="contact-list">
      <li class="contact-item">
        <svg class="contact-icon" viewBox="0 0 30 30" aria-hidden="true">
          <rect x="9" y="3" width="12" height="24" rx="2.5" fill="none" stroke="#fff" stroke-width="2"/>
          <circle cx="15" cy="23" r="1.6" fill="#fff"/>
        </svg>
        <span>000-5550147</span>
      </li>
      <li class="contact-item">
        <svg class="contact-icon" viewBox="0 0 30 30" aria-hidden="true">
          <rect x="4" y="8" width="22" height="15" rx="1.5" fill="none" stroke="#fff" stroke-width="2"/>
          <polyline points="4,9 15,17 26,9" fill="none" stroke="#fff" stroke-width="2"/>
        </svg>
        <span>info@maplelectern.com</span>
      </li>
      <li class="contact-item">
        <svg class="contact-icon" viewBox="0 0 30 30" aria-hidden="true">
          <circle cx="15" cy="15" r="13" fill="var(--icon-fill)" stroke="#fff" stroke-width="1.5"/>
        </svg>
        <span>Social : @maplelectern</span>
      </li>
      <li class="contact-item">
        <svg class="contact-icon" viewBox="0 0 30 30" aria-hidden="true">
          <circle cx="15" cy="15" r="13" fill="var(--icon-fill)" stroke="#fff" stroke-width="1.5"/>
        </svg>
        <span>Call: maple.lectern</span>
      </li>
      <li class="contact-item is-phone-alt">
        <svg class="contact-icon" viewBox="0 0 30 30" aria-hidden="true">
          <path d="M4 12 Q15 4 26 12 L23 15 L19 13 L19 10 Q15 9 11 10 L11 13 L7 15 Z" fill="#fff"/>
          <rect x="8" y="17" width="14" height="9" rx="2" fill="#fff"/>
        </svg>
        <span>000-5550199</span>
      </li>
    </ul>

    <address class="address">
      Address:<br>
      H 48 Birch Lane, Kingsford province and country
    </address>
  </article>
</main>
</body>
</html>
```